"Harrow Crest Builders" is a residential building company and needs a new business card design and may re

We would like a redesign based on the existing logo, and would like to see a new font as well. We are bespoke home builders who build sustainable energy efficient homes.

Industry/Entity Type

Construction

Contact Information for Business Card

Business card size 40mm x 90mm

Colors

Designer to choose colors to be used in the design.

```html
<!DOCTYPE html>
<html lang="en">
<head>
<meta charset="utf-8">
<title>Harrow Crest Builders – Business Card</title>
<link rel="stylesheet" href="https://fonts.googleapis.com/css2?family=Roboto:wght@400;500;700&family=Roboto+Condensed:wght@700&display=swap">
<style>
  :root {
    --backdrop: #e4e2de;
    --card-light: #f3f3f2;
    --card-dark: #1b1c1e;
    --lime: #b5cf32;
    --ink: #1c1c1c;
    --ink-soft: #4a4a4a;
  }
  html, body {
    margin: 0;
    padding: 0;
    width: 1200px;
    height: 960px;
    overflow: hidden;
    background: var(--backdrop);
  }
  .canvas {
    position: relative;
    width: 1200px;
    height: 960px;
    font-family: "Roboto", Arial, sans-serif;
  }
  .card {
    position: absolute;
    width: 601px;
    height: 341px;
    box-shadow: 0 3px 8px rgba(0,0,0,0.35);
    overflow: hidden;
  }
  .card--front { left: 302px; top: 130px; background: var(--card-light); }
  .card--back  { left: 299px; top: 489px; background: var(--card-dark); }

  .brand-band {
    position: absolute;
    left: 0; top: 58px;
    width: 30px; height: 26px;
    background: var(--lime);
  }
  .brand-name {
    position: absolute;
    left: 38px; top: 52px;
    margin: 0;
    font-weight: 700;
    font-size: 27px;
    color: var(--ink);
    letter-spacing: -0.2px;
    line-height: 1;
  }
  .details {
    position: absolute;
    left: 139px; top: 112px;
    color: var(--ink-soft);
    font-size: 14.5px;
    line-height: 18px;
  }
  .details__person {
    margin: 0 0 12px;
    font-family: "Roboto Condensed", "Arial Narrow", sans-serif;
    font-weight: 700;
    font-size: 22px;
    line-height: 26px;
    color: var(--ink);
  }
  .details p { margin: 0; }
  .details__company { font-weight: 500; }
  .details__block { margin-bottom: 3px; }
  .contact { list-style: none; margin: 5px 0 0; padding: 0; }
  .contact li { display: flex; align-items: center; height: 19.5px; }
  .contact svg { width: 12px; height: 13px; margin-right: 10px; fill: var(--ink); }

  .back-mark {
    position: absolute;
    left: 0; right: 0; top: 150px;
    display: flex;
    justify-content: center;
    align-items: center;
    gap: 14px;
  }
  .back-mark__square { width: 22px; height: 22px; background: var(--lime); }
  .back-mark__name {
    margin: 0;
    font-weight: 700;
    font-size: 34px;
    color: var(--lime);
    line-height: 1;
  }
  .back-web {
    position: absolute;
    left: 0; right: 0; top: 295px;
    margin: 0;
    text-align: center;
    color: var(--lime);
    font-size: 14px;
    letter-spacing: 2.6px;
  }
</style>
</head>
<body>
<main class="canvas">
  <section class="card card--front" aria-label="Card front">
    <div class="brand-band"></div>
    <h1 class="brand-name">Harrow Crest Builders</h1>
    <div class="details">
      <h2 class="details__person">DANIEL VORTREY</h2>
      <div class="details__block">
        <p class="details__company">Harrow Crest Builders Pty Ltd</p>
        <p>PO Box 4120 Lakeview</p>
        <p>LPO Ashdale WA 6099</p>
      </div>
      <div class="details__block">
        <p>Registration 40873</p>
        <p>ABN: 42 913 205 768</p>
      </div>
      <ul class="contact">
        <li>
          <svg viewBox="0 0 12 14" aria-hidden="true"><path d="M3 0h6a1.5 1.5 0 0 1 1.5 1.5v11A1.5 1.5 0 0 1 9 14H3a1.5 1.5 0 0 1-1.5-1.5v-11A1.5 1.5 0 0 1 3 0zm0 2v9h6V2zm3 9.6a.8.8 0 1 0 0 1.6.8.8 0 0 0 0-1.6z"/></svg>
          0412 555 019
        </li>
        <li>
          <svg viewBox="0 0 12 14" aria-hidden="true"><path d="M0 3.5h12v8H0zm1.2 1.2v.3L6 8l4.8-3v-.3zm0 1.7v3.9h9.6V6.4L6 9.4z"/></svg>
          daniel@harrowcrestbuilders.com.au
        </li>
        <li>
          <svg viewBox="0 0 12 14" aria-hidden="true"><path d="M6 1a6 6 0 1 0 0 12A6 6 0 0 0 6 1zm-1 2.2c.6.6.4 1.4-.3 1.7-.7.3-.6 1 0 1.4.7.5.4 1.5-.4 1.6-.9.1-1.6.7-1.5 1.6A4.6 4.6 0 0 1 5 3.2zm2.3.1a4.6 4.6 0 0 1 3.2 3.9c-.6-.3-1.3-.2-1.7.4-.4.6-1.1.5-1.3-.2-.2-.8-.9-1-1.3-1.6-.3-.6.4-1 .9-1.2.4-.2.4-.8.2-1.3z"/></svg>
          www.harrowcrestbuilders.com.au
        </li>
      </ul>
    </div>
  </section>

  <section class="card card--back" aria-label="Card back">
    <div class="back-mark">
      <span class="back-mark__square"></span>
      <p class="back-mark__name">Harrow Crest Builders</p>
    </div>
    <p class="back-web">www.harrowcrestbuilders.com.au</p>
  </section>
</main>
</body>
</html>
```